LEARN Business Skills so you can Earn a good living

size of the poster is 8”x 10.75" plus 0.25" bleed.
Please leave 1 inch on the bottoum for footer
I want a design a poster that will attract people's attention.
I appreciate a creative ad however the ad should not take away from being able to clearly read the text.
-I also appreciate a simple creative ad that is not too busy.
-you can use graphics, vectors, or pictures of real people.
-however, if you use real people it should be a white male that is wearing a white shirt and look like a professional person.

Target Market(s)

Potential young business people

Industry/Entity Type

education

Requirements
Must have
• easy to read the text
Nice to have
• I would like a "creative" simple ad that is easy to be read
Should not have
• pictures of women

```html
<!DOCTYPE html>
<html lang="en">
<head>
<meta charset="utf-8">
<title>Learn It to Earn It – Business Enrichment Course</title>
<link href="https://fonts.googleapis.com/css2?family=Montserrat:wght@500;600;700;800;900&family=Poppins:wght@800&display=swap" rel="stylesheet">
<style>
  :root {
    --mat: #5c5c5c;
    --navy: #1d2758;
    --deep-teal: #2e5f7e;
    --teal: #52c3bd;
    --gold: #efb944;
    --white: #ffffff;
    --ink: #131a3f;
    --cream: #fef9c2;
  }
  * { margin: 0; padding: 0; box-sizing: border-box; }
  html, body { width: 1200px; height: 1200px; overflow: hidden; background: var(--mat); }
  .poster {
    position: absolute; left: 205px; top: 100px; width: 790px; height: 1000px; overflow: hidden;
    background: linear-gradient(90deg, var(--navy) 0%, #2a4c74 30%, var(--deep-teal) 45%, var(--teal) 72%, var(--teal) 100%);
    font-family: "Montserrat", sans-serif;
  }
  .photo-money {
    position: absolute; left: 25px; top: 240px; width: 545px; height: 300px;
    border-radius: 50% 50% 0 0 / 70% 70% 0 0;
    background: radial-gradient(ellipse at 55% 45%, #d9dccd 0%, #a9b09a 55%, #7f8772 100%);
  }
  .photo-person {
    position: absolute; left: 490px; top: 16px; width: 300px; height: 510px;
    border-radius: 140px 140px 0 0;
    background: linear-gradient(180deg, #d7a98a 0%, #c9d6ea 28%, #b8c9e4 70%, #8a8062 100%);
  }
  .chevron { position: absolute; left: 0; top: 0; }
  .headline {
    position: absolute; left: 52px; top: 58px;
    font-weight: 800; font-size: 92px; line-height: 78px; letter-spacing: -1px; color: var(--white);
  }
  .headline .accent { color: var(--gold); }
  .headline .lower { font-weight: 600; }
  .badge {
    position: absolute; left: 47px; top: 354px; width: 220px; height: 220px; border-radius: 50%;
    background: var(--gold); display: flex; align-items: center; justify-content: center; text-align: center;
    font-family: "Poppins", sans-serif; font-weight: 800; font-size: 28px; line-height: 30px; color: #111;
  }
  .benefit { position: absolute; top: 595px; width: 240px; text-align: center; }
  .benefit .icon {
    width: 102px; height: 102px; border-radius: 50%; background: var(--white); margin: 0 auto;
    display: flex; align-items: center; justify-content: center;
  }
  .benefit p { margin-top: 18px; font-weight: 500; font-size: 19px; line-height: 23px; color: var(--white); }
  .benefit-trust { left: 23px; }
  .benefit-skills { left: 244px; }
  .benefit-income { left: 496px; }
  .divider { position: absolute; top: 718px; height: 64px; border-left: 2px dotted rgba(255,255,255,0.8); }
  .topics {
    position: absolute; left: 40px; top: 814px; width: 710px; text-align: center;
    font-weight: 800; font-size: 8.6px; line-height: 11px; color: var(--white); letter-spacing: 0.1px;
  }
  .footer-box { position: absolute; left: 46px; top: 860px; width: 698px; height: 93px; background: var(--cream); }
</style>
</head>
<body>
<main class="poster">
  <div class="photo-money" role="img" aria-label="Pile of dollar bills behind an open laptop"></div>
  <div class="photo-person" role="img" aria-label="Smiling young businessman in a light shirt typing on a laptop"></div>

  <svg class="chevron" width="790" height="1000" viewBox="0 0 790 1000" aria-hidden="true">
    <defs>
      <linearGradient id="bandFill" x1="0" x2="1" y1="0" y2="0">
        <stop offset="0" stop-color="#5cc7c1"/>
        <stop offset="0.45" stop-color="#7fd5cf"/>
        <stop offset="0.62" stop-color="#e9f7f6"/>
        <stop offset="1" stop-color="#c6ecea"/>
      </linearGradient>
    </defs>
    <path d="M0 412 L471 550 L790 464 L790 520 L475 604 L0 472 Z" fill="url(#bandFill)"/>
  </svg>

  <h1 class="headline">
    <span class="accent">LEARN</span> IT<br>
    <span class="lower">to</span> <span class="accent">EARN</span> IT
  </h1>

  <div class="badge">Business<br>Enrichment<br>Course</div>

  <section class="benefit benefit-trust">
    <div class="icon">
      <svg width="64" height="64" viewBox="0 0 64 64" fill="none" stroke="var(--ink)" stroke-width="4" stroke-linejoin="round" stroke-linecap="round">
        <path d="M8 30 L24 12 L34 16 L46 10 L56 22 L36 46 C32 50 28 50 24 46 L12 36 Z"/>
        <path d="M20 32 L30 42 M26 26 L36 36 M32 20 L42 30"/>
      </svg>
    </div>
    <p>A proven success<br>of helping people<br>in their livelihoods</p>
  </section>
  <div class="divider" style="left:268px"></div>

  <section class="benefit benefit-skills">
    <div class="icon">
      <svg width="74" height="74" viewBox="0 0 74 74" fill="none" stroke="var(--ink)" stroke-width="3.5" stroke-linejoin="round">
        <circle cx="22" cy="22" r="10"/><circle cx="22" cy="22" r="4"/>
        <path d="M22 6v6M22 32v6M6 22h6M32 22h6M11 11l4 4M29 29l4 4M11 33l4-4M29 15l4-4"/>
        <circle cx="48" cy="50" r="13"/><circle cx="48" cy="50" r="5"/>
        <path d="M48 30v7M48 63v7M28 50h7M61 50h7M34 36l5 5M57 59l5 5M34 64l5-5M57 41l5-5"/>
      </svg>
    </div>
    <p>Business<br>skills that will<br>help you</p>
  </section>
  <div class="divider" style="left:460px"></div>

  <section class="benefit benefit-income">
    <div class="icon">
      <svg width="68" height="68" viewBox="0 0 68 68" fill="none" stroke="var(--ink)" stroke-width="4" stroke-linejoin="round">
        <rect x="16" y="14" width="46" height="30" rx="2"/>
        <circle cx="39" cy="29" r="6" fill="var(--ink)"/>
        <path d="M10 20v30h46M4 26v30h46"/>
      </svg>
    </div>
    <p>Get a quality job - start/<br>grow your business-<br>Increase your salary</p>
  </section>

  <p class="topics">
    BUSINESS ADMIISTRATION – SMALL BUSINESS MANAGEMENT - FINANCE - INVESTMENTS - COMPUTERS- ACCOUNTING - SALES - MARKETING<br>
    - PROJECT MANAGEMENT INTERVIEWING SKILLS - BUSINESS LAW -NEGOTIATION -- PUBLIC SPEAKING - &nbsp;- IMPORT/EXPORT - INFORMATION<br>
    TECHNOLOY -DISTRIBUTION - MARKETING - &nbsp;LEDGERPRO - REAL ESTATE - HEALTH CARE-MANAGEMENT - SHOPVERSE
  </p>

  <div class="footer-box"></div>
</main>
</body>
</html>
```